Job Recruiting Agemcy

almost like my current site www.pkvtl.net but with these changes see and what i meant about the across the to the site says home job companies categories pages blog and login sign up that should only be the 4 i said only 1 home 2 industries 3 jobs 4 contact us. and remove latest blog post and our partners because that's not us we have to post acuarte information thanks and the name of the company if your using is is work and careful staffing partners and want it easy for us to post and remove jobs and where it emails us every resume or person that applies

Requirements
Must have
• must send email to us when an application is submitted and try to incorparate the colors of current site
Nice to have
• i want a pretty basic site for now just like the one i have but with all thats above were its easy for me being the own to be able to post jobs and everything

```html
<!DOCTYPE html>
<html lang="en">
<head>
<meta charset="utf-8">
<title>PKVTL – work and careful staffing partners</title>
<link rel="stylesheet" href="https://fonts.googleapis.com/css2?family=Orbitron:wght@700;900&family=Roboto:wght@400;500;700&display=swap">
<style>
:root{
  --purple:#7a1fd6;
  --purple-deep:#5b14c4;
  --magenta:#a8238f;
  --magenta-dark:#7c1870;
  --ink:#1d1d24;
  --muted:#6b6b78;
  --hero-bg:#e3e3ee;
  --line:#e4e4ea;
  --white:#ffffff;
}
*{margin:0;padding:0;box-sizing:border-box}
html,body{width:1200px;height:3256px;overflow:hidden}
body{font-family:"Roboto",Arial,sans-serif;color:var(--ink);background:var(--white);position:relative}
.heading{font-family:"Orbitron","Roboto",sans-serif;font-weight:900;letter-spacing:3px;text-transform:uppercase}
.btn{display:inline-block;font-size:13px;font-weight:700;text-transform:uppercase;letter-spacing:.5px;padding:12px 22px;border-radius:3px}
.btn-solid{background:linear-gradient(90deg,var(--magenta),var(--purple));color:var(--white)}
.btn-outline{border:2px solid var(--magenta);color:var(--magenta);background:var(--white)}
.brand{font-weight:700;color:var(--purple);letter-spacing:2px}

/* header + hero */
.hero{position:absolute;left:0;top:0;width:1200px;height:680px;background:var(--hero-bg);overflow:hidden}
.hero-photo{position:absolute;right:0;top:0;width:560px;height:680px;background:linear-gradient(160deg,#d9d3ea 0%,#c6bedb 55%,#b9b1cf 100%)}
.site-header{position:absolute;left:0;top:0;width:1200px;height:110px}
.logo{position:absolute;left:152px;top:34px;display:flex;align-items:center;gap:10px}
.logo-square{width:26px;height:26px;background:var(--purple)}
.logo .brand{font-size:26px}
.main-nav{position:absolute;left:552px;top:40px;display:flex;gap:30px}
.main-nav a{font-size:13px;font-weight:500;color:var(--ink);text-decoration:none;text-transform:uppercase}
.main-nav a.active{color:var(--magenta);border-bottom:2px solid var(--magenta);padding-bottom:4px}
.signup{position:absolute;left:920px;top:30px;padding:10px 22px}
.hero-kicker{position:absolute;left:144px;top:238px;font-size:17px;font-weight:500;color:var(--purple);text-transform:uppercase}
.hero-title{position:absolute;left:144px;top:272px;font-size:60px;line-height:66px;color:var(--ink)}
.search-bar{position:absolute;left:144px;top:446px;width:540px;height:48px;background:var(--white);display:flex;align-items:center;border-radius:3px;box-shadow:0 2px 8px rgba(0,0,0,.08)}
.search-field{flex:1;height:100%;display:flex;align-items:center;justify-content:space-between;padding:0 14px;font-size:13px;color:var(--muted);border-right:1px solid var(--line)}
.search-bar .btn{height:36px;margin:0 6px;padding:10px 20px}
.slider-dots{position:absolute;left:144px;top:562px;display:flex;gap:8px}
.slider-dots span{width:9px;height:9px;border-radius:50%;background:#b6b4c6}
.slider-dots span:first-child{background:var(--purple)}

/* about */
.about{position:absolute;left:0;top:680px;width:1200px;height:480px}
.about-mark{position:absolute;left:200px;top:60px;width:240px;height:340px;display:flex;align-items:center;justify-content:center;gap:12px}
.about-mark .logo-square{width:40px;height:40px}
.about-mark .brand{font-size:46px}
.about-title{position:absolute;left:512px;top:62px;font-size:40px}
.about-text{position:absolute;left:512px;top:130px;width:520px;font-size:12.5px;line-height:20px;color:var(--muted)}
.about .btn{position:absolute;left:512px;top:340px}

/* industries */
.industries{position:absolute;left:0;top:1160px;width:1200px;height:340px;display:flex}
.industry{position:relative;width:300px;height:340px}
.industry:nth-child(1){background:linear-gradient(160deg,#5b6170,#2a2d36)}
.industry:nth-child(2){background:linear-gradient(160deg,#8aa2b8,#3a4654)}
.industry:nth-child(3){background:linear-gradient(160deg,#7f6c68,#2a2f3c)}
.industry:nth-child(4){background:linear-gradient(160deg,#9eb0c0,#4a5662)}
.industry p{position:absolute;left:18px;bottom:18px;width:260px;color:var(--white);font-size:12.5px;font-weight:700;line-height:17px;text-transform:uppercase}

/* jobs */
.jobs-title{position:absolute;left:0;top:1598px;width:1200px;text-align:center;font-size:40px}
.job-card{position:absolute;width:412px;height:160px;background:var(--white);border:1px solid var(--line);box-shadow:0 2px 10px rgba(0,0,0,.05)}
.job-card .company-icon{position:absolute;left:24px;top:28px;width:34px;height:34px;border-radius:50%;background:#ececf2}
.job-card h3{position:absolute;left:84px;top:24px;width:280px;font-size:16px;line-height:20px;font-weight:700}
.job-card .tag{position:absolute;left:84px;top:76px;background:#f1eef8;color:var(--muted);font-size:11px;padding:5px 10px;border-radius:3px}
.job-card .meta{position:absolute;left:84px;top:112px;font-size:11px;color:var(--muted)}
.job-card .bookmark{position:absolute;right:18px;top:20px}
.jobs-more{position:absolute;left:528px;top:2092px}

/* testimonial */
.testimonial{position:absolute;left:0;top:2228px;width:1200px;height:316px;background:linear-gradient(90deg,var(--magenta-dark),var(--magenta) 50%,var(--magenta-dark))}
.testimonial .avatar{position:absolute;left:168px;top:92px;width:132px;height:132px;border-radius:50%;border:5px solid var(--white);background:linear-gradient(160deg,#c9b9ac,#7a6a64)}
.testimonial blockquote{position:absolute;left:330px;top:88px;width:700px;color:var(--white);font-size:17px;line-height:25px;font-style:italic}
.testimonial cite{position:absolute;left:330px;top:200px;color:var(--white);font-size:14px;font-style:normal}
.testimonial cite b{font-weight:700}
.arrow{position:absolute;top:142px}

/* seeking */
.seeking-title{position:absolute;left:144px;top:2592px;font-size:40px}
.seeking-text{position:absolute;left:144px;top:2652px;font-size:14px;color:var(--muted)}
.seeking-actions{position:absolute;left:144px;top:2690px;display:flex;gap:16px}
.seeking-photo{position:absolute;left:740px;top:2556px;width:360px;height:196px;background:linear-gradient(170deg,#e6e8ee,#b9c2cf)}

/* footer */
.site-footer{position:absolute;left:0;top:2752px;width:1200px;height:504px;background:linear-gradient(180deg,var(--purple-deep),var(--purple));color:var(--white);text-align:center}
.footer-logo{position:absolute;left:0;top:72px;width:1200px;display:flex;justify-content:center;align-items:center;gap:10px}
.footer-logo .logo-square{background:var(--white)}
.footer-logo .brand{color:var(--white);font-size:28px}
.footer-logo-sub{position:absolute;left:0;top:120px;width:1200px;font-size:10px;letter-spacing:1px;text-transform:uppercase}
.footer-nav{position:absolute;left:0;top:232px;width:1200px;display:flex;justify-content:center;gap:14px;font-size:18px;font-weight:500}
.footer-legal{position:absolute;left:0;top:282px;width:1200px;font-size:11px;opacity:.9}
.footer-social{position:absolute;left:0;top:326px;width:1200px;display:flex;justify-content:center;gap:16px}
.footer-social span{width:18px;height:18px;border-radius:50%;background:var(--white)}
</style>
</head>
<body>

<section class="hero">
  <div class="hero-photo" role="img" aria-label="Smiling woman in a blue shirt holding a laptop"></div>
  <header class="site-header">
    <div class="logo"><span class="logo-square"></span><span class="brand">PKVTL</span></div>
    <nav class="main-nav">
      <a class="active">Home</a><a>Industries</a><a>Jobs</a><a>Contact us</a>
    </nav>
    <a class="btn btn-solid signup">Sign up</a>
  </header>
  <p class="hero-kicker">Search from job offers</p>
  <h1 class="heading hero-title">Your career<br>starts here!</h1>
  <div class="search-bar">
    <div class="search-field">Keywords <svg width="10" height="6"><path d="M0 0l5 6 5-6z" fill="#888"/></svg></div>
    <div class="search-field">Location <svg width="10" height="6"><path d="M0 0l5 6 5-6z" fill="#888"/></svg></div>
    <a class="btn btn-solid">Search</a>
  </div>
  <div class="slider-dots"><span></span><span></span><span></span><span></span></div>
</section>

<section class="about">
  <div class="about-mark"><span class="logo-square"></span><span class="brand">PKVTL</span></div>
  <h2 class="heading about-title">About us</h2>
  <p class="about-text">We have over 15 years of specialized recruiting and staffing experience. We cover a broad spectrum of industries, from aerospace to pharmaceutical and cosmetics companies of every size. Our team works closely with each client to understand its culture and needs, and each candidate to understand their goals. We match skilled people with the right roles, handle screening with care, and stay in touch long after placement. Honest advice, steady follow-up and accurate information guide every search we run.</p>
  <a class="btn btn-solid">Read more</a>
</section>

<section class="industries">
  <div class="industry" role="img" aria-label="Aerospace workshop photo"><p>Aero space - Orvane Flight Controls, Stellix, Corvane Electric</p></div>
  <div class="industry" role="img" aria-label="Laboratory scientist photo"><p>Pharmaceutical/ Biotechnology Verdal Bio, Lumera Cosmetics</p></div>
  <div class="industry" role="img" aria-label="Trucks on a highway at sunset"><p>Transportation - Halvern Freight, Parcelway</p></div>
  <div class="industry" role="img" aria-label="Medical staff in a clinic"><p>Medical - Medrin, Tessaly Care</p></div>
</section>

<h2 class="heading jobs-title">Recent jobs</h2>
<article class="job-card" style="left:176px;top:1700px">
  <span class="company-icon"></span><h3>Lorem ipsum dolor sit amet consectetur adipiscing</h3>
  <span class="tag">Flexible hours and paid overtime</span><span class="meta">3 days ago · Full time</span>
  <svg class="bookmark" width="10" height="13"><path d="M0 0h10v13l-5-4-5 4z" fill="#7a1fd6"/></svg>
</article>
<article class="job-card" style="left:608px;top:1700px">
  <span class="company-icon"></span><h3>Lorem ipsum dolor sit amet consectetur adipiscing</h3>
  <span class="tag">Flexible hours and paid overtime</span><span class="meta">2 days ago · Full time</span>
  <svg class="bookmark" width="10" height="13"><path d="M0 0h10v13l-5-4-5 4z" fill="#7a1fd6"/></svg>
</article>
<article class="job-card" style="left:176px;top:1888px">
  <span class="company-icon"></span><h3>Lorem ipsum dolor sit amet consectetur adipiscing</h3>
  <span class="tag">Flexible hours and paid overtime</span><span class="meta">4 days ago · Full time</span>
  <svg class="bookmark" width="10" height="13"><path d="M0 0h10v13l-5-4-5 4z" fill="#7a1fd6"/></svg>
</article>
<article class="job-card" style="left:608px;top:1888px">
  <span class="company-icon"></span><h3>Lorem ipsum dolor sit amet consectetur adipiscing</h3>
  <span class="tag">Flexible hours and paid overtime</span><span class="meta">5 days ago · Full time</span>
  <svg class="bookmark" width="10" height="13"><path d="M0 0h10v13l-5-4-5 4z" fill="#7a1fd6"/></svg>
</article>
<a class="btn btn-solid jobs-more">View more</a>

<section class="testimonial">
  <svg class="arrow" style="left:100px" width="20" height="34"><path d="M18 2L3 17l15 15" stroke="#fff" stroke-width="3" fill="none"/></svg>
  <div class="avatar" role="img" aria-label="Portrait of a client"></div>
  <blockquote>Lorem ipsum dolor sit amet, consectetur adipiscing elit, sed do eiusmod tempor incididunt ut labore et dolore magna aliqua ipsum suspendisse ultrices gravida commodo viverra maecenas accumsan lacus vel facilisem ipsum dolor sit amet</blockquote>
  <cite>– <b>JOHN DOE</b> Customer</cite>
  <svg class="arrow" style="left:1080px" width="20" height="34"><path d="M2 2l15 15L2 32" stroke="#fff" stroke-width="3" fill="none"/></svg>
</section>

<h2 class="heading seeking-title">Seeking for a job?</h2>
<p class="seeking-text">Browse hundreds of job offers and find the most suitable position.</p>
<div class="seeking-actions"><a class="btn btn-solid">Search jobs</a><a class="btn btn-outline">Add a resume</a></div>
<div class="seeking-photo" role="img" aria-label="Two professionals looking at a laptop"></div>

<footer class="site-footer">
  <div class="footer-logo"><span class="logo-square"></span><span class="brand">PKVTL</span></div>
  <p class="footer-logo-sub">work and careful staffing partners</p>
  <nav class="footer-nav"><span>HOME</span><span>/</span><span>INDUSTRIES</span><span>/</span><span>JOBS</span><span>/</span><span>CONTACT US</span></nav>
  <p class="footer-legal">© 2020 pkvtl All rights reserved &nbsp;|&nbsp; Privacy Policy &nbsp;|&nbsp; Terms and Use</p>
  <div class="footer-social"><span></span><span></span><span></span></div>
</footer>

</body>
</html>
```